Business Card for a Wedding Films Business

We require a business card design for our business 'Lewis Marrow Wedding Films'. The logo needs to look classy and high end.

Target Market(s)

Wedding Couples

Contact Information for Business Card

Lewis Marrow Wedding Films
07312 605 227
films@lewismarrowreels.com
www.lewismarrowreels.com

Facebook: @lewismarrowweddingfilms
Instagram: @lewismarrowfilms

Font styles to use
Sans Serif

Requirements
Must have
• Social media icons - Facebook and Instagram

```html
<!DOCTYPE html>
<html lang="en">
<head>
<meta charset="utf-8">
<title>Lewis Marrow Wedding Films – Business Card</title>
<link href="https://fonts.googleapis.com/css2?family=Jost:wght@500&family=Arimo:wght@400&display=swap" rel="stylesheet">
<style>
  :root {
    --backdrop: #d6d6d6;
    --ink: #000000;
    --paper: #ffffff;
    --silver: #b9b9b9;
  }
  html, body {
    margin: 0;
    padding: 0;
    width: 1200px;
    height: 801px;
    overflow: hidden;
    background: var(--backdrop);
  }
  .canvas {
    position: relative;
    width: 1200px;
    height: 801px;
  }
  .card {
    position: absolute;
    top: 274px;
    width: 443px;
    height: 263px;
    overflow: hidden;
  }
  .card--back {
    left: 153px;
    background: var(--ink);
    color: var(--paper);
  }
  .card--front {
    left: 625px;
    background: var(--paper);
    color: var(--ink);
  }
  .contact-list {
    position: absolute;
    left: 28px;
    top: 75px;
    margin: 0;
    padding: 0;
    list-style: none;
    font-family: "Arimo", Arial, sans-serif;
    font-size: 12.2px;
    line-height: 15.7px;
  }
  .contact-list li {
    display: flex;
    align-items: center;
    gap: 6px;
  }
  .contact-list .gap-before {
    margin-top: 21px;
  }
  .contact-icon {
    width: 12px;
    height: 12px;
    flex: none;
  }
  .back-name {
    position: absolute;
    right: 14px;
    bottom: 18px;
    font-family: "Jost", Arial, sans-serif;
    font-weight: 500;
    font-size: 30px;
    line-height: 1.05;
    letter-spacing: 3px;
    text-align: right;
    color: var(--silver);
    text-transform: uppercase;
  }
  .wordmark {
    position: absolute;
    left: 0;
    right: 0;
    top: 150px;
    text-align: center;
    font-family: "Jost", Arial, sans-serif;
    font-weight: 500;
    text-transform: uppercase;
  }
  .wordmark__name {
    display: block;
    font-size: 24px;
    letter-spacing: 5px;
    line-height: 1;
  }
  .wordmark__tagline {
    display: block;
    margin-top: 7px;
    font-size: 11px;
    letter-spacing: 4.6px;
    line-height: 1;
  }
</style>
</head>
<body>
<main class="canvas">
  <section class="card card--back" aria-label="Card back with contact details">
    <ul class="contact-list">
      <li>
        <svg class="contact-icon" viewBox="0 0 12 12" aria-hidden="true"><path d="M2.3 1h2l1 2.6-1.3.9a6.5 6.5 0 0 0 3.5 3.5l.9-1.3 2.6 1v2a1 1 0 0 1-1 1A9.5 9.5 0 0 1 1.3 2a1 1 0 0 1 1-1z" fill="none" stroke="#fff" stroke-width="1.2"/></svg>
        07312 605 227
      </li>
      <li>
        <svg class="contact-icon" viewBox="0 0 12 12" aria-hidden="true"><rect x="0.5" y="2.5" width="11" height="7.5" fill="#fff"/><path d="M0.8 2.8 6 7l5.2-4.2" fill="none" stroke="#000" stroke-width="0.9"/></svg>
        films@lewismarrowreels.com
      </li>
      <li>
        <svg class="contact-icon" viewBox="0 0 12 12" aria-hidden="true"><g fill="none" stroke="#fff" stroke-width="0.9"><circle cx="6" cy="6" r="5.2"/><ellipse cx="6" cy="6" rx="2.3" ry="5.2"/><path d="M0.8 6h10.4M1.6 3.4h8.8M1.6 8.6h8.8"/></g></svg>
        www.lewismarrowreels.com
      </li>
      <li class="gap-before">
        <svg class="contact-icon" viewBox="0 0 12 12" aria-hidden="true"><rect x="0.5" y="0.5" width="11" height="11" rx="1.5" fill="#fff"/></svg>
        @lewismarrowweddingfilms
      </li>
      <li>
        <svg class="contact-icon" viewBox="0 0 12 12" aria-hidden="true"><rect x="0.8" y="0.8" width="10.4" height="10.4" rx="2.5" fill="none" stroke="#fff" stroke-width="1.2"/></svg>
        @lewismarrowfilms
      </li>
    </ul>
    <div class="back-name">Lewis<br>Marrow</div>
  </section>

  <section class="card card--front" aria-label="Card front with business name">
    <h1 class="wordmark">
      <span class="wordmark__name">Lewis Marrow</span>
      <span class="wordmark__tagline">Wedding Films</span>
    </h1>
  </section>
</main>
</body>
</html>
```